New Business Card Design Project

We need to enhance the look and feel of our brand. We are starting with the business card and will hopefully expand to letter head, website, etc. The firm is based in Kolding Denmark and invests with global pension funds and for mutual fund investors alike. We would like to see an innovative use of the companies logo (star on the website - www.northmerrowcap.com) and a broader use of a color palette. Presently it is dominantly shades of blue. The firm wants to convey a sense they are a creative investment team that understands all the risks in the emerging markets and have the skills to perform in an environment of uncertainty.

Presently, we have three locations: Kolding Denmark, Glendale CA USA, Zurich Switzerland. We also have a prominently displayed bar code square on a solid dark blue back that will take smart phone users to the firm's website. I am indifferent to its inclusion., Details for my new Business Card Design Project will be added soon.
Updates

Project Deadline Extended
Reason: Designers, I am working with on getting feedback from both US and Danish partners on preferences. That is taking slightly more time than expected. Thanks for you patience. Nice work. TLV

Target Market(s)

The target market is a combination of institutional and retail investors. The european arm uses a card similar to a couple of those submitted.

Industry/Entity Type

Environment

Requirements
Must have
• The company's Star Logo. See www.northmerrowcap.com. It may be used in its current form or some new clever way. The founders are Danish and have a strong affinity for it.
Nice to have
• The new materials may be solely used in the north America and distributed in Australia as well. Therefore, we may try something new in these markets. I'd prefer to see a broader use of the color spectrum, not simply blue.
Should not have
• The card should not look and feel like a bank, insurance company, or a traditional money manager.

```html
<!DOCTYPE html>
<html lang="da">
<head>
<meta charset="utf-8">
<title>North Merrow – Business Card</title>
<link rel="stylesheet" href="https://fonts.googleapis.com/css2?family=Aldrich&family=Barlow:wght@500&display=swap">
<style>
  :root {
    --navy: #04335c;
    --sky: #3aa6e0;
    --paper: #ffffff;
    --ink: #0d3a63;
    --stage: #8c8c8c;
  }
  html, body {
    margin: 0;
    padding: 0;
    width: 1200px;
    height: 659px;
    overflow: hidden;
    background: var(--stage);
  }
  .stage {
    position: relative;
    width: 1200px;
    height: 659px;
  }
  .card {
    position: absolute;
    width: 480px;
    height: 280px;
    background: var(--paper);
    box-shadow: 0 6px 18px rgba(0,0,0,0.35);
    overflow: hidden;
  }
  .card-front { left: 70px; top: 190px; }
  .card-back { left: 650px; top: 190px; }
  .card .waves {
    position: absolute;
    inset: 0;
    width: 480px;
    height: 280px;
  }
  .wave-navy { fill: var(--navy); }
  .wave-sky { fill: var(--sky); }

  .brand {
    position: absolute;
    left: 0;
    right: 0;
    top: 72px;
    display: flex;
    flex-direction: column;
    align-items: center;
    gap: 8px;
  }
  .brand-mark {
    width: 60px;
    height: 60px;
    border-radius: 50%;
    background: var(--sky);
    border: 4px solid var(--navy);
    box-sizing: border-box;
  }
  .brand-name {
    font-family: "Aldrich", sans-serif;
    font-size: 36px;
    line-height: 1;
    color: var(--navy);
  }

  .company {
    position: absolute;
    left: 24px;
    top: 70px;
    margin: 0;
    font-family: "Aldrich", sans-serif;
    font-size: 18px;
    font-weight: 400;
    color: var(--navy);
    white-space: nowrap;
  }
  .icon-tab {
    position: absolute;
    left: 0;
    top: 108px;
    width: 36px;
    height: 116px;
    background: var(--sky);
    border-radius: 0 6px 6px 0;
  }
  .icon-tab svg {
    position: absolute;
    left: 10px;
    width: 16px;
    height: 16px;
    fill: none;
    stroke: var(--paper);
    stroke-width: 1.6;
  }
  .contact {
    position: absolute;
    left: 46px;
    top: 112px;
    margin: 0;
    padding: 0;
    list-style: none;
    font-family: "Barlow", sans-serif;
    font-weight: 500;
    font-size: 13.5px;
    color: var(--ink);
    line-height: 25px;
  }
  .contact .fax-label { margin: 0 4px 0 10px; }
  .social {
    position: absolute;
    right: 22px;
    top: 226px;
    display: flex;
    gap: 4px;
  }
  .social span {
    width: 16px;
    height: 16px;
    border-radius: 2px;
    background: var(--sky);
  }
  .social span:nth-child(1) { background: #6b5a4e; }
  .social span:nth-child(2) { background: #3b5a9a; }
  .social span:nth-child(3) { background: #1d75b0; }
</style>
</head>
<body>
<main class="stage">

  <section class="card card-front" aria-label="Card front">
    <svg class="waves" viewBox="0 0 480 280" aria-hidden="true">
      <path class="wave-sky" d="M0 0H480V30C360 32 160 34 0 16Z"/>
      <path class="wave-navy" d="M0 0H480V20C360 24 160 22 0 8Z"/>
      <path class="wave-sky" d="M0 280V244C160 250 330 228 480 248V280Z"/>
      <path class="wave-navy" d="M0 280V254C160 258 330 240 480 262V280Z"/>
    </svg>
    <div class="brand">
      <span class="brand-mark"></span>
      <span class="brand-name">North Merrow</span>
    </div>
  </section>

  <section class="card card-back" aria-label="Card back">
    <svg class="waves" viewBox="0 0 480 280" aria-hidden="true">
      <path class="wave-sky" d="M0 0H480V92C380 86 220 30 0 22Z"/>
      <path class="wave-navy" d="M0 0H480V80C380 74 220 20 0 12Z"/>
      <path class="wave-sky" d="M0 280V228C160 226 330 250 480 270V280Z"/>
      <path class="wave-navy" d="M0 280V238C160 236 330 260 480 280Z"/>
    </svg>

    <h1 class="company">North Merrow Fondsmæglerselskab A/S</h1>

    <div class="icon-tab" aria-hidden="true">
      <svg viewBox="0 0 16 16" style="top:8px"><path d="M8 15C4 10 3 8 3 6a5 5 0 0 1 10 0c0 2-1 4-5 9Z"/><circle cx="8" cy="6" r="1.6"/></svg>
      <svg viewBox="0 0 16 16" style="top:36px"><path d="M4 2l2.5 3-1.5 1.5c1 2 2.5 3.5 4.5 4.5L11 9.5l3 2.5-1.5 2C7 13 3 9 2 3.5Z"/></svg>
      <svg viewBox="0 0 16 16" style="top:64px"><rect x="1.5" y="3.5" width="13" height="9"/><path d="M1.5 3.5L8 9l6.5-5.5"/></svg>
      <svg viewBox="0 0 16 16" style="top:92px"><circle cx="8" cy="8" r="6.5"/><path d="M1.5 8h13M8 1.5c-3 3.5-3 9.5 0 13M8 1.5c3 3.5 3 9.5 0 13"/></svg>
    </div>

    <ul class="contact">
      <li>Strandvej 14 · DK-8700 Horsens</li>
      <li>45-70-00-10-10<span class="fax-label">Fax</span>45-70-00-10-20</li>
      <li>post@northmerrowcap.com</li>
      <li>www.northmerrowcap.com</li>
    </ul>

    <div class="social" aria-label="Social profiles">
      <span></span><span></span><span></span><span></span>
    </div>
  </section>

</main>
</body>
</html>
```